Ferris Contracting LLC Business Card Design

I am looking for a creative and unique business card design. We are a commercial construction general contractor. With the name "FERRIS" Contracting, I am hoping to see some neat designs that correlate with the name.

```html
<!DOCTYPE html>
<html lang="en">
<head>
<meta charset="utf-8">
<title>Ferris Contracting LLC – Business Card</title>
<link rel="stylesheet" href="https://fonts.googleapis.com/css2?family=Mulish:wght@400;800&family=Playfair+Display:ital,wght@0,400;1,400&display=swap">
<style>
  :root {
    --backdrop: #262b31;
    --card: #f7f8f8;
    --brand-blue: #2f7fc0;
    --steel: #9a9fa4;
    --ink: #2a2d31;
    --name-grey: #8b8d90;
    --title-navy: #3d5873;
    --icon-blue: #4f88b8;
    --rule: #a9adb1;
  }
  * { box-sizing: border-box; margin: 0; padding: 0; }
  html, body {
    width: 1200px;
    height: 575px;
    overflow: hidden;
    background: var(--backdrop);
  }
  .card {
    position: absolute;
    top: 138px;
    width: 509px;
    height: 328px;
    background: var(--card);
  }
  .card--front { left: 70px; }
  .card--back { left: 621px; }

  /* Front: company name */
  .brand {
    position: absolute;
    inset: 0;
    display: flex;
    align-items: center;
    justify-content: center;
    gap: 18px;
  }
  .brand__dot {
    width: 64px;
    height: 64px;
    border-radius: 50%;
    background: var(--steel);
    flex: none;
  }
  .brand__name {
    font-family: "Mulish", sans-serif;
    font-weight: 800;
    color: var(--brand-blue);
    line-height: 1;
  }
  .brand__word {
    display: block;
    font-size: 72px;
    letter-spacing: 1px;
  }
  .brand__sub {
    display: block;
    font-size: 21px;
    letter-spacing: 6.5px;
    margin-top: 6px;
  }

  /* Back: identity */
  .identity {
    position: absolute;
    right: 34px;
    top: 34px;
    text-align: right;
    font-family: "Playfair Display", serif;
  }
  .identity__tagline {
    font-size: 14px;
    color: var(--title-navy);
    line-height: 1;
  }
  .identity__name {
    font-size: 34px;
    color: var(--name-grey);
    line-height: 1.15;
    margin-top: 6px;
  }
  .identity__role {
    font-size: 21px;
    font-style: italic;
    color: var(--title-navy);
    line-height: 1.1;
  }
  .divider {
    position: absolute;
    left: 35px;
    right: 34px;
    top: 137px;
    height: 3px;
    background: linear-gradient(90deg, #8f9398, var(--rule) 50%, #c9ccd0);
  }

  /* Back: contact list */
  .contacts {
    position: absolute;
    right: 34px;
    top: 158px;
    list-style: none;
    font-family: "Mulish", sans-serif;
    font-size: 19px;
    color: var(--ink);
    text-align: right;
  }
  .contacts__item {
    display: flex;
    justify-content: flex-end;
    align-items: flex-start;
    gap: 14px;
    line-height: 29px;
  }
  .contacts__icon {
    width: 18px;
    height: 18px;
    margin-top: 5px;
    flex: none;
    fill: none;
    stroke: var(--icon-blue);
    stroke-width: 1.8;
  }
  .contacts__icon--solid { fill: var(--icon-blue); stroke: none; }
</style>
</head>
<body>
  <section class="card card--front">
    <div class="brand">
      <span class="brand__dot"></span>
      <p class="brand__name">
        <span class="brand__word">FERRIS</span>
        <span class="brand__sub">CONTRACTING</span>
      </p>
    </div>
  </section>

  <section class="card card--back">
    <header class="identity">
      <p class="identity__tagline">[A refined sansseris name]</p>
      <h1 class="identity__name">Dana Whitfield</h1>
      <p class="identity__role">Principal</p>
    </header>
    <div class="divider"></div>
    <ul class="contacts">
      <li class="contacts__item">
        <span>503.555.0142</span>
        <svg class="contacts__icon" viewBox="0 0 18 18" aria-hidden="true"><rect x="5" y="1.5" width="8" height="15" rx="1.5"/><line x1="8" y1="14" x2="10" y2="14"/></svg>
      </li>
      <li class="contacts__item">
        <span>dana.w@ferris-contracting.com</span>
        <svg class="contacts__icon contacts__icon--solid" viewBox="0 0 18 18" aria-hidden="true"><path d="M1 4h16v10H1z"/><path d="M1 4l8 6 8-6" fill="none" stroke="#f7f8f8" stroke-width="1.4"/></svg>
      </li>
      <li class="contacts__item">
        <span>www.ferris-contracting.com</span>
        <svg class="contacts__icon" viewBox="0 0 18 18" aria-hidden="true"><circle cx="9" cy="9" r="7.5"/><ellipse cx="9" cy="9" rx="3.3" ry="7.5"/><line x1="1.5" y1="9" x2="16.5" y2="9"/></svg>
      </li>
      <li class="contacts__item">
        <span>88 Millrace Road, Suite 210<br>Portland, OR 97209</span>
        <svg class="contacts__icon contacts__icon--solid" viewBox="0 0 18 18" aria-hidden="true"><path d="M9 1a5.5 5.5 0 0 0-5.5 5.5C3.5 11 9 17 9 17s5.5-6 5.5-10.5A5.5 5.5 0 0 0 9 1zm0 7.7a2.2 2.2 0 1 1 0-4.4 2.2 2.2 0 0 1 0 4.4z"/></svg>
      </li>
    </ul>
  </section>
</body>
</html>
```